Machine Sign

This is for a laundromat. I would like signs to hang above the machines from the ceiling indicating machine size. For example we have 6 loaders, 4 loaders, 2 loaders.

```html
<!DOCTYPE html>
<html lang="en">
<head>
<meta charset="utf-8">
<title>Machine Sign – 4 Loaders</title>
<link rel="stylesheet" href="https://fonts.googleapis.com/css2?family=Montserrat:wght@700&display=swap">
<style>
  :root {
    --page-bg: #ecebee;
    --sign-base: #24084a;
    --bubble-magenta: #d0207a;
    --bubble-blue: #2c6fe0;
    --bubble-violet: #6a22c9;
    --bubble-teal: #23b7c8;
    --label-fill: #ffffff;
    --label-outline: #1d0638;
  }
  * { margin: 0; padding: 0; box-sizing: border-box; }
  html, body {
    width: 1200px;
    height: 900px;
    overflow: hidden;
    background: var(--page-bg);
  }
  .canvas {
    position: relative;
    width: 1200px;
    height: 900px;
    display: flex;
    align-items: center;
    justify-content: center;
  }
  .machine-sign {
    position: relative;
    width: 1140px;
    height: 810px;
    background: var(--sign-base);
    overflow: hidden;
    box-shadow: 0 6px 24px rgba(0, 0, 0, 0.18);
  }
  .bubble-artwork {
    position: absolute;
    inset: 0;
    background:
      radial-gradient(circle at 12% 14%, rgba(208, 32, 122, 0.55) 0, rgba(44, 111, 224, 0.35) 12%, transparent 22%),
      radial-gradient(circle at 83% 24%, rgba(208, 32, 122, 0.55) 0, rgba(44, 111, 224, 0.35) 13%, transparent 24%),
      radial-gradient(circle at 22% 78%, rgba(106, 34, 201, 0.6) 0, rgba(44, 111, 224, 0.4) 18%, transparent 34%),
      radial-gradient(circle at 52% 40%, rgba(35, 183, 200, 0.35) 0, rgba(106, 34, 201, 0.3) 12%, transparent 24%),
      radial-gradient(circle at 80% 92%, rgba(106, 34, 201, 0.55) 0, rgba(208, 32, 122, 0.3) 12%, transparent 24%),
      var(--sign-base);
  }
  .size-label {
    position: absolute;
    left: 0;
    right: 0;
    text-align: center;
    font-family: "Montserrat", sans-serif;
    font-weight: 700;
    color: var(--label-fill);
    -webkit-text-stroke: 8px var(--label-outline);
    paint-order: stroke fill;
    line-height: 1;
  }
  .size-number {
    top: 60px;
    font-size: 440px;
    left: 10px;
  }
  .size-word {
    top: 450px;
    font-size: 196px;
    left: 78px;
    letter-spacing: 1px;
  }
</style>
</head>
<body>
  <main class="canvas">
    <section class="machine-sign">
      <div class="bubble-artwork" role="img" aria-label="Iridescent soap bubbles in magenta, blue and violet floating on a deep purple background"></div>
      <p class="size-label size-number">4</p>
      <p class="size-label size-word">LOADERS</p>
    </section>
  </main>
</body>
</html>
```